Education / Investment Website Design (PDF Wireframe Provided)

More details are in the wireframe document

We need a website design for an investment education company. Our Clients purchase education courses through us. We use meridian toolkit (Wordpress) for our website. We just require the graphics in PSD (not coded) for the

1. Homepage - brightfunnelhub.com style
2. Blog page - brightfunnelhub.com style
3. Single Blog Post
4. Product page - Lernova.com style
5. Single Product Page - https://www.lernova.com/share-market-class-oceania/?ref=kP7qLmW3xT9Z
6. Contact Us Page (Contact Us Form, Map and Contact details)
7. About Us Page

See the attached Wireframe for the homepage

IMPORTANT
Websites we like are clean, white, similar to BrightFunnelHub.com and Lernova.com
Use of white space, big fonts, flat buttons

Attached wireframe is the flow of the homepage. (Homepage brief PDF)

Each section represents a "fold" as visitors are scrolling down. (Homepage showing folds PDF - how the visitor sees each section of the homepage as they scroll down the homepage)

We've got a clear idea of the elements on the page and looking for a great graphic / web designer to create those for us. (We do the coding)

Website currently is: southerncrosswealthschool.com.au (we want to simplify the website and have a more modern / flat design)

Questions: Please ask

Target Market(s)

Investors, People looking for Investment / Financial Education

Industry/Entity Type

Investment

Number of Pages Required

5+ page

Font styles to use
Sans Serif

Requirements
Must have
• Similar Items listed in the wireframe
• Clean Look - Flat design - elegant
• Roll-over (mouse on / mouse off) for Buttons and Top Banner Selection
Should not have
• Images that looks too much like "Stock Images"
• Please avoid bright orange

```html
<!DOCTYPE html>
<html lang="en">
<head>
<meta charset="utf-8">
<title>Southern Cross Wealth School</title>
<link href="https://fonts.googleapis.com/css2?family=PT+Sans:wght@400;700&family=Lato:wght@400;700&display=swap" rel="stylesheet">
<style>
:root{
  --navy:#2b3050;
  --navy-dark:#23273f;
  --grey-band:#e1e1e1;
  --page-grey:#efefef;
  --teal:#53b5b0;
  --teal-panel:rgba(86,196,178,.86);
  --green:#5bcf9f;
  --blue:#4a86c5;
  --btn-blue:#3d9bd0;
  --ink:#1b1b1b;
  --muted:#6a6a6a;
  --footer:#262626;
  --footer-bottom:#1c1c1c;
  --footer-text:#bdbdbd;
  --white:#ffffff;
}
*{box-sizing:border-box;margin:0;padding:0}
html,body{width:1200px;height:2436px;overflow:hidden}
body{position:relative;background:var(--white);font-family:"PT Sans",Arial,sans-serif;color:var(--ink)}
.abs{position:absolute}

.notice-bar{left:0;top:0;width:1200px;height:26px;background:var(--navy);color:#fff;font-family:"Lato",Arial,sans-serif;font-size:13px;line-height:26px;padding-left:110px}
.notice-bar em{color:#5fd3c6;font-weight:700}
.notice-close{right:110px;top:8px;width:11px;height:11px;border-radius:50%;background:#7b8097}

.utility-bar{left:0;top:26px;width:1200px;height:45px;background:var(--grey-band)}
.search-box{left:110px;top:9px;width:247px;height:27px;background:#fff;border:1px solid #cfcfcf;font-size:12px;color:#a0a0a0;line-height:25px;padding-left:12px}
.search-box svg{position:absolute;right:8px;top:6px}
.social-top{right:110px;top:9px;display:flex;gap:8px}
.social-top span{width:27px;height:27px;background:var(--navy)}

.main-nav{left:0;top:71px;width:1200px;height:95px;background:#fff}
.brand{left:110px;top:22px;display:flex;align-items:center;gap:10px}
.brand-dot{width:44px;height:44px;border-radius:50%;background:var(--navy)}
.brand-name{font-size:19px;font-weight:700;color:var(--navy);line-height:1.05;letter-spacing:.5px}
.nav-links{left:378px;top:38px;display:flex;font-size:15px;color:var(--ink)}
.nav-links a{color:inherit;text-decoration:none;margin-right:44px}
.btn-signin{left:921px;top:35px;width:81px;height:30px;background:var(--navy);color:#fff;font-size:14px;text-align:center;line-height:30px}
.btn-join{left:1008px;top:35px;width:82px;height:30px;background:var(--green);color:#fff;font-size:14px;text-align:center;line-height:30px}

.hero{left:0;top:166px;width:1200px;height:601px;background:linear-gradient(110deg,#2f4a2a 0%,#4c6a3c 25%,#6b5a44 50%,#a87a48 75%,#d99a4c 100%)}
.hero-panel{left:190px;top:154px;width:830px;height:309px;background:var(--teal-panel);border-radius:3px}
.hero-title{left:0;top:33px;width:830px;text-align:center;color:#fff;font-size:44px}
.hero-search{left:44px;top:118px;width:687px;height:56px;background:#fff;font-size:20px;color:#777;line-height:56px;padding-left:20px}
.hero-search-btn{left:731px;top:118px;width:57px;height:56px;background:var(--blue)}
.hero-search-btn svg{position:absolute;left:18px;top:17px}
.stat{display:flex;align-items:center;gap:14px;top:212px;color:#234;font-size:16px;line-height:1.2}

.courses{left:0;top:767px;width:1200px;height:974px;background:var(--page-grey)}
.section-title{left:0;width:1200px;text-align:center;font-size:44px;color:var(--ink)}
.section-sub{left:0;width:1200px;text-align:center;font-size:28px;color:var(--muted)}
.course-card{width:350px;height:303px;background:#fff;box-shadow:0 1px 3px rgba(0,0,0,.18)}
.card-art{left:0;top:0;width:350px;height:130px}
.art-analytics{background:linear-gradient(135deg,#7cc8e4,#5bb4d8)}
.art-banking{background:linear-gradient(135deg,#2f5b78,#234a63)}
.art-mobile{background:linear-gradient(135deg,#c4d94a,#aac73a)}
.card-title{left:13px;top:148px;font-size:23px;color:var(--ink)}
.card-text{left:13px;top:178px;width:330px;font-size:13.5px;line-height:16px;color:#333}
.card-btn{left:15px;top:255px;width:107px;height:30px;background:var(--btn-blue);color:#fff;font-size:14px;text-align:center;line-height:30px;border-bottom:2px solid #2f7fae}
.browse-bar{left:52px;top:859px;width:1101px;height:73px;background:var(--teal);color:#fff;font-size:36px;text-align:center;line-height:73px;letter-spacing:.5px}

.cta{left:0;top:1741px;width:1200px;height:245px;background:#fff}
.cta-title{left:0;top:52px;width:1200px;text-align:center;font-size:42px}
.cta-sub{left:0;top:104px;width:1200px;text-align:center;font-size:27px;color:var(--muted)}
.cta-btn{left:520px;top:151px;width:151px;height:63px;background:var(--navy);color:#fff;font-size:26px;text-align:center;line-height:63px;border-radius:5px}

.footer{left:0;top:1986px;width:1200px;height:404px;background:var(--footer);color:var(--footer-text)}
.footer-brand{left:60px;top:50px;display:flex;align-items:center;gap:10px}
.footer-brand .brand-dot{width:44px;height:44px;background:#fff}
.footer-brand .brand-name{color:#fff}
.footer-tag{left:60px;top:110px;width:230px;font-size:12px;line-height:19px}
.footer-col h4{font-weight:400;font-size:20px;color:#fff;margin-bottom:6px}
.footer-col ul{list-style:none;font-size:12px;line-height:20px}
.footer-social{display:flex;gap:8px;margin-top:10px}
.footer-social span{width:27px;height:27px;border-radius:50%;background:#6b6b6b}
.notice-title{left:60px;top:197px;font-size:16px;font-weight:700;color:#fff}
.notice-text{left:60px;top:226px;width:1100px;font-size:11.6px;line-height:20px;color:#d4d4d4}
.notice-text b{color:#fff}
.notice-address{left:60px;top:342px;font-size:12px;color:#fff}
.footer-bottom{left:0;top:2390px;width:1200px;height:46px;background:var(--footer-bottom);color:#fff;font-size:12.5px;line-height:46px}
.copyright{left:60px}
.legal-links{right:60px;word-spacing:2px}
</style>
</head>
<body>

<div class="abs notice-bar">First time visitor?&nbsp; Then <em>start here</em> and learn more about Southern Cross Wealth School!
  <span class="abs notice-close"></span>
</div>

<div class="abs utility-bar">
  <div class="abs search-box">Search...
    <svg width="14" height="14" viewBox="0 0 14 14"><circle cx="6" cy="6" r="4.5" fill="none" stroke="#999" stroke-width="1.6"/><line x1="9.5" y1="9.5" x2="13" y2="13" stroke="#999" stroke-width="1.8"/></svg>
  </div>
  <div class="abs social-top" aria-label="Social links"><span></span><span></span><span></span><span></span></div>
</div>

<header class="abs main-nav">
  <div class="abs brand"><span class="brand-dot"></span><span class="brand-name">Southern Cross<br>Wealth School</span></div>
  <nav class="abs nav-links"><a href="#">Home</a><a href="#">Blogs</a><a href="#">Products</a><a href="#">About Us</a><a href="#">Members</a><a href="#">Contact Us</a></nav>
  <div class="abs btn-signin">Sign In</div>
  <div class="abs btn-join">Join Us</div>
</header>

<section class="abs hero" role="img" aria-label="Photo of a person at a cafe table using a tablet beside a coffee cup">
  <div class="abs hero-panel">
    <h1 class="abs hero-title" style="font-weight:400">Your place to learn real world skills online.</h1>
    <div class="abs hero-search">What do you want to learn today?</div>
    <div class="abs hero-search-btn"><svg width="22" height="22" viewBox="0 0 22 22"><circle cx="9" cy="9" r="6.5" fill="none" stroke="#fff" stroke-width="3"/><line x1="14" y1="14" x2="20" y2="20" stroke="#fff" stroke-width="3.4"/></svg></div>
    <div class="abs stat" style="left:106px">
      <svg width="50" height="32" viewBox="0 0 50 32" fill="#25304a"><circle cx="25" cy="8" r="7"/><circle cx="11" cy="11" r="5"/><circle cx="39" cy="11" r="5"/><path d="M13 32c0-9 5-15 12-15s12 6 12 15z"/><path d="M2 30c0-7 4-11 9-11 2 0 3 .5 4 1-3 3-4 6-4 10z"/><path d="M48 30c0-7-4-11-9-11-2 0-3 .5-4 1 3 3 4 6 4 10z"/></svg>
      <span>Over 6 million<br>students.</span></div>
    <div class="abs stat" style="left:305px">
      <svg width="40" height="32" viewBox="0 0 40 32" fill="none" stroke="#25304a" stroke-width="2.4"><path d="M20 6C15 2 8 2 2 4v24c6-2 13-2 18 2 5-4 12-4 18-2V4c-6-2-13-2-18 2z"/><line x1="20" y1="6" x2="20" y2="30"/></svg>
      <span>More than<br>25,000 courses!</span></div>
    <div class="abs stat" style="left:520px">
      <svg width="26" height="36" viewBox="0 0 26 36" fill="none" stroke="#25304a" stroke-width="2.4"><rect x="2" y="2" width="22" height="32" rx="3"/><line x1="6" y1="10" x2="20" y2="10"/><line x1="6" y1="16" x2="20" y2="16"/><line x1="6" y1="22" x2="16" y2="22"/><circle cx="13" cy="29" r="1.4" fill="#25304a"/></svg>
      <span>Learn at your pace on<br>any device.</span></div>
  </div>
</section>

<section class="abs courses">
  <h2 class="abs section-title" style="top:60px;font-weight:400">Cources and Advanced Training</h2>
  <p class="abs section-sub" style="top:106px">Your Trading Resource for Success</p>

  <article class="abs course-card" style="left:52px;top:177px">
    <div class="abs card-art art-analytics" role="img" aria-label="Illustration of a desktop screen with bar chart and magnifying glass"></div>
    <h3 class="abs card-title" style="font-weight:400">Forex and Trading Made Easy</h3>
    <p class="abs card-text">Lorem ipsum dolor sit amet consectetur adipi-scing elit sed do eiusmod tempor incididunt ut labore et dolore a magna aliqua ut enim ad minim</p>
    <div class="abs card-btn">Learn More</div>
  </article>
  <article class="abs course-card" style="left:425px;top:177px">
    <div class="abs card-art art-banking" role="img" aria-label="Illustration of a bank building over a world map with currency symbols"></div>
    <h3 class="abs card-title" style="font-weight:400">Forex and Trading Made Easy</h3>
    <p class="abs card-text">Lorem ipsum dolor sit amet consectetur adipi-scing elit sed do eiusmod tempor incididunt ut labore et dolore a magna aliqua ut enim ad minim</p>
    <div class="abs card-btn">Learn More</div>
  </article>
  <article class="abs course-card" style="left:802px;top:177px">
    <div class="abs card-art art-mobile" role="img" aria-label="Illustration of a hand holding a smartphone surrounded by app icons"></div>
    <h3 class="abs card-title" style="font-weight:400">Forex and Trading Made Easy</h3>
    <p class="abs card-text">Lorem ipsum dolor sit amet consectetur adipi-scing elit sed do eiusmod tempor incididunt ut labore et dolore a magna aliqua ut enim ad minim</p>
    <div class="abs card-btn">Learn More</div>
  </article>

  <article class="abs course-card" style="left:52px;top:511px">
    <div class="abs card-art art-analytics" role="img" aria-label="Illustration of a desktop screen with bar chart and magnifying glass"></div>
    <h3 class="abs card-title" style="font-weight:400">Forex and Trading Made Easy</h3>
    <p class="abs card-text">Lorem ipsum dolor sit amet consectetur adipi-scing elit sed do eiusmod tempor incididunt ut labore et dolore a magna aliqua ut enim ad minim</p>
    <div class="abs card-btn">Learn More</div>
  </article>
  <article class="abs course-card" style="left:425px;top:511px">
    <div class="abs card-art art-banking" role="img" aria-label="Illustration of a bank building over a world map with currency symbols"></div>
    <h3 class="abs card-title" style="font-weight:400">Forex and Trading Made Easy</h3>
    <p class="abs card-text">Lorem ipsum dolor sit amet consectetur adipi-scing elit sed do eiusmod tempor incididunt ut labore et dolore a magna aliqua ut enim ad minim</p>
    <div class="abs card-btn">Learn More</div>
  </article>
  <article class="abs course-card" style="left:802px;top:511px">
    <div class="abs card-art art-mobile" role="img" aria-label="Illustration of a hand holding a smartphone surrounded by app icons"></div>
    <h3 class="abs card-title" style="font-weight:400">Forex and Trading Made Easy</h3>
    <p class="abs card-text">Lorem ipsum dolor sit amet consectetur adipi-scing elit sed do eiusmod tempor incididunt ut labore et dolore a magna aliqua ut enim ad minim</p>
    <div class="abs card-btn">Learn More</div>
  </article>

  <div class="abs browse-bar">Browse Courses</div>
</section>

<section class="abs cta">
  <h2 class="abs cta-title" style="font-weight:400">Ready to master some skills?</h2>
  <p class="abs cta-sub">Take your career to the next level!</p>
  <div class="abs cta-btn">Sign Up</div>
</section>

<footer class="abs footer">
  <div class="abs footer-brand"><span class="brand-dot"></span><span class="brand-name">Southern Cross<br>Wealth School</span></div>
  <p class="abs footer-tag">SwiftTrade is a registered trademark of Bastion Ridge Trading Ltd.</p>

  <div class="abs footer-col" style="left:388px;top:42px"><h4>Main Menu</h4>
    <ul><li>Home</li><li>Cources</li><li>Blog</li><li>About Us</li><li>Contact Us</li></ul></div>
  <div class="abs footer-col" style="left:603px;top:42px"><h4>Cources</h4>
    <ul><li>Foundation</li><li>OME</li><li>Stock</li><li>futures</li><li>Mindset</li></ul></div>
  <div class="abs footer-col" style="left:801px;top:42px"><h4>Others</h4>
    <ul><li>FSG</li><li>Disclaimers</li><li>Other Legal</li></ul></div>
  <div class="abs footer-col" style="left:970px;top:42px"><h4>Connect With Us</h4>
    <div class="footer-social" aria-label="Social links"><span></span><span></span><span></span><span></span><span></span></div></div>

  <h4 class="abs notice-title">CUSTOMER NOTICE</h4>
  <p class="abs notice-text"><b>SOUTHERN CROSS WEALTH SCHOOL PTY LTD</b> is an authorised representative (AR 402117) of OCEANIC MARKETS ADVISORY SERVICES PTY LTD - ACN 612 048 779 (AFSL 518260). SCW is authorised to provide general advice in Securities and Derivatives. No consideration has been given or will be given to the individual investment objectives, financial situation or needs of any particular person. The decision to invest or trade and the method selected is a personal decision and involves an inherent level of risk, and you must undertake your own investigations and obtain your own advice regarding the suitability of this product for your circumstances. Please be aware that all trading activity is subject to both profit &amp; loss and may not be suitable for you. Please Click Here to view the SCW Financial Services Guide.</p>
  <p class="abs notice-address">Southern Cross Wealth School Pty Ltd | Address: Harbourview House, Level 2, 48 Shoreline Drive, Eastport, QLD 4300 | Phone: 1300 555 018</p>
</footer>

<div class="abs footer-bottom">
  <span class="abs copyright">Copyright © 2015. Kestrel Studio .All rights reserved.</span>
  <span class="abs legal-links">Terms &amp; Conditions &nbsp;&nbsp; | &nbsp;&nbsp; Privacy Policy</span>
</div>

</body>
</html>
```